4 Page 8.5x11 Price List & Flyer

Our main product price list that goes out to all of our dealers and distributors both in print and PDF. Should be clean and bright, easy to read and attract attention.
Updates

Target Market(s)

Dealers and distributors of sports card holders, photo holders, sports memorabilia display cases, etc.

Industry/Entity Type

Product

Requirements
Must have
• Paperstone Crest logo, photos

```html
<!DOCTYPE html>
<html lang="en">
<head>
<meta charset="utf-8">
<title>Price List – Soft Sleeves &amp; Display Cases</title>
<link href="https://fonts.googleapis.com/css2?family=Great+Vibes&family=Arimo:wght@400&display=swap" rel="stylesheet">
<style>
  :root{
    --gold:#c9a646;
    --gold-dark:#a9862c;
    --frame:#0d0d0d;
    --paper:#ffffff;
    --ink:#111111;
    --sky-top:#5f8fa3;
    --sky-mid:#b9cfd6;
    --ground:#a6a7a9;
    --photo-dark:#2a2c30;
    --photo-light:#b7bcc2;
    --ball:#7a4128;
  }
  *{box-sizing:border-box;margin:0;padding:0}
  html,body{width:1200px;height:1200px;overflow:hidden}
  body{
    position:relative;
    background:linear-gradient(180deg,var(--sky-top) 0%,#8fb1bf 30%,var(--sky-mid) 55%,#c4c6c8 60%,var(--ground) 66%,var(--ground) 100%);
    font-family:"Arimo",Arial,sans-serif;color:var(--ink);
  }
  .frame{position:absolute;left:0;top:0}
  .sheet{
    position:absolute;left:62px;top:54px;width:1076px;height:1064px;
    background:var(--paper);border:2px solid var(--frame);
  }
  .section-title{
    position:absolute;left:0;width:100%;text-align:center;
    font-family:"Great Vibes",cursive;font-size:74px;line-height:1;color:var(--ink);
  }
  .title-sleeves{top:88px}
  .title-cases{top:724px}
  .product-photo{position:absolute;border-radius:4px}
  .photo-pack{width:62px;height:102px;background:linear-gradient(180deg,var(--photo-dark) 0%,#4a4d52 20%,#6d7277 50%,var(--photo-dark) 100%)}
  .photo-helmet{width:134px;height:104px;background:linear-gradient(180deg,#d8dde2,var(--photo-dark) 55%,#b08f3a)}
  .photo-football{width:108px;height:104px;background:radial-gradient(ellipse at 50% 45%,var(--ball) 0%,#5b2f1c 45%,var(--photo-light) 72%,#e4e6e8 100%)}
  table.price-table{position:absolute;border-collapse:collapse;font-size:14px;line-height:1.1}
  .price-table th,.price-table td{border:1.5px solid var(--frame);padding:1px 4px;vertical-align:top}
  .price-table th{font-weight:400;font-size:19px;text-align:center;vertical-align:middle}
  .sleeves-table{left:99px;top:138px;width:914px}
  .sleeves-table td{height:19px}
  .sleeves-table td.tall{height:41px}
  .sleeves-table td.pack,.sleeves-table td.price{text-align:center}
  .cases-table{left:101px;top:781px;width:888px}
  .cases-table td{height:22.5px}
  .cases-table td.price{text-align:right;padding-right:6px}
  .cases-table th{height:30px}
</style>
</head>
<body>
  <svg class="frame" width="1200" height="1200" viewBox="0 0 1200 1200" aria-hidden="true">
    <g fill="none" stroke-linejoin="miter">
      <polygon points="40,40 1160,40 1160,540 1182,590 1160,640 1160,1132 40,1132 40,640 18,590 40,540" stroke="var(--gold)" stroke-width="46"/>
      <polygon points="40,40 1160,40 1160,540 1182,590 1160,640 1160,1132 40,1132 40,640 18,590 40,540" stroke="var(--frame)" stroke-width="40"/>
      <polygon points="40,40 1160,40 1160,540 1182,590 1160,640 1160,1132 40,1132 40,640 18,590 40,540" stroke="var(--gold)" stroke-width="14"/>
      <polygon points="40,40 1160,40 1160,540 1182,590 1160,640 1160,1132 40,1132 40,640 18,590 40,540" stroke="var(--frame)" stroke-width="9"/>
    </g>
  </svg>

  <main class="sheet">
    <div class="product-photo photo-pack" style="left:160px;top:24px" role="img" aria-label="Photo of a packaged stack of soft card sleeves"></div>
    <div class="product-photo photo-pack" style="left:850px;top:24px" role="img" aria-label="Photo of a packaged stack of soft card sleeves"></div>
    <h1 class="section-title title-sleeves" style="top:26px">Soft Sleeves</h1>

    <table class="price-table sleeves-table">
      <colgroup><col style="width:266px"><col style="width:229px"><col style="width:251px"><col style="width:168px"></colgroup>
      <tr><th>Description</th><th>Pack/Case/Weight</th><th>$250 Min</th><th>$1,500 Min</th></tr>
      <tr><td>Soft Card Sleeves</td><td class="pack">100/10000/14 lbs</td><td class="price">$25/case</td><td class="price">$23/case</td></tr>
      <tr><td>Thick Card Soft Sleeves</td><td class="pack">100/10000/16 lbs</td><td class="price">$35/case</td><td class="price">$32/case</td></tr>
      <tr><td class="tall">Team Set Bags – Resealable</td><td class="pack">100/5000/14 lbs</td><td class="price">$42.50/case</td><td class="price">$39/case</td></tr>
      <tr><td>Graded Bags – Resealable</td><td class="pack">100/5000/15 lbs</td><td class="price">$49/case</td><td class="price">$42/case</td></tr>
      <tr><td>Postcard Soft Sleeves</td><td class="pack">100/5000/14 lbs</td><td class="price">$35/case</td><td class="price">$32/case</td></tr>
      <tr><td>4x6 Photo Soft Sleeves</td><td class="pack">100/5000/16 lbs</td><td class="price">$42/case</td><td class="price">$36/case</td></tr>
      <tr><td>5x7 Photo Soft Sleeves</td><td class="pack">100/5000/20 lbs</td><td class="price">$55/case</td><td class="price">$49/case</td></tr>
      <tr><td>8x10 Photo Soft Sleeves</td><td class="pack">100/1000/16 lbs</td><td class="price">$24/case</td><td class="price">$21/case</td></tr>
      <tr><td>Card Keeper 1</td><td class="pack">200/2000/30 lbs</td><td class="price">$75/case</td><td class="price">$69/case</td></tr>
      <tr><td>Card Keeper 2</td><td class="pack">200/2000/25 lbs</td><td class="price">$59/case</td><td class="price">$52/case</td></tr>
      <tr><td>Card Keeper 3</td><td class="pack">100/1000/12 lbs</td><td class="price">$60/case</td><td class="price">$55/case</td></tr>
      <tr><td>Card Keeper 4</td><td class="pack">100/1000/26 lbs</td><td class="price">$110/case</td><td class="price">$100/case</td></tr>
      <tr><td>Card Keeper 5</td><td class="pack">100/1000/24 lbs</td><td class="price">$95/case</td><td class="price">$89/case</td></tr>
      <tr><td class="tall">Semi Rigid Bill Saver 1 – Reg. Currency</td><td class="pack">50/500/14 lbs</td><td class="price">$35/case</td><td class="price">$29/case</td></tr>
      <tr><td class="tall">Semi Rigid Bill Saver 2 – Large Currency</td><td class="pack">50/500/17 lbs</td><td class="price">$42/case</td><td class="price">$35/case</td></tr>
      <tr><td class="tall">Baseball Bat Tubes-Black Cap</td><td class="pack">1/24/33 lbs</td><td class="price">$2.95</td><td class="price">$2.75</td></tr>
    </table>

    <div class="product-photo photo-helmet" style="left:118px;top:654px" role="img" aria-label="Photo of a football helmet in an acrylic display case"></div>
    <div class="product-photo photo-football" style="left:810px;top:656px" role="img" aria-label="Photo of a football in an acrylic display case"></div>
    <h2 class="section-title title-cases" style="top:668px">Display Cases</h2>

    <table class="price-table cases-table">
      <colgroup><col style="width:592px"><col style="width:151px"><col style="width:145px"></colgroup>
      <tr><th>Description</th><th>$250 Min</th><th>$1,500 Min</th></tr>
      <tr><td>Deluxe Acrylic Football Case w/ Gold Risers &amp; Mirrored Back</td><td class="price">$23.50 each</td><td class="price">$21.50 Each</td></tr>
      <tr><td>Above – Wall Mount Version</td><td class="price">$25.50 each</td><td class="price">$23.00 Each</td></tr>
      <tr><td>Deluxe Acrylic FS Helmet Case w/ Gold Risers &amp; Mirrored Back</td><td class="price">$33.50 each</td><td class="price">$31.50 Each</td></tr>
      <tr><td>Deluxe Acrylic Mini Helmet Case w/ Gold Risers &amp; Mirror Back</td><td class="price">$14.50 each</td><td class="price">$13.50 Each</td></tr>
      <tr><td>Above – Wall Mount Version</td><td class="price">$15.50 each</td><td class="price">$14.50 Each</td></tr>
      <tr><td>Deluxe Acrylic Basketball Case w/ Gold Risers &amp; Mirror Back</td><td class="price">$29.00 each</td><td class="price">$26.50 Each</td></tr>
      <tr><td>Golden Mitt Baseball Display w/ Black Acrylic Base, Case/6</td><td class="price">$7.50 each</td><td class="price">$6.75 Each</td></tr>
      <tr><td>Deluxe Acrylic Cap/Hat Case w/ Gold Risers &amp; Mirrored Back</td><td class="price">$20.50 each</td><td class="price">$19.50 Each</td></tr>
      <tr><td>Above – Wall Mount Version</td><td class="price">$22.00 each</td><td class="price">$20.50 Each</td></tr>
      <tr><td>Deluxe Acrylic Baseball Bat Case (Wall Mount or Table Top)</td><td class="price">$49.00 each</td><td class="price">$45.00 Each</td></tr>
    </table>
  </main>
</body>
</html>
```